Core Values Poster for Healthcare company

Trying to Create a core values poster for my company. Healthcare Company - We have Neurosurgery, Pain Management, Physical Therapy, Occupational Therapy, Rehab, Imaging, and psychology so far and we are growing fast.

Core Values would Include - (Execution), (Loyalty), (Innovation), (Synergy), (Growth-Oriented), (Ethics & Integrity), (Love), and (Energy)

Please incorporate the Company Logo which is on the website and I have included it in my uploads. As long as the logo stays blue it does not need a gradient effect.

I like the posters made for this contest : https://pinlarkstudio.com.au/flyer-work/briefs/build-team-ideals-flyer-580316

This picture should be memorable so people know our Core Values

Target Market(s)

Staff in the company

Colors

Designer to choose colors to be used in the design.

Requirements
Must have
• Logo
Nice to have
• Pictures for each core value

```html
<!DOCTYPE html>
<html lang="en">
<head>
<meta charset="utf-8">
<title>Clearview – Core Values</title>
<link rel="stylesheet" href="https://fonts.googleapis.com/css2?family=Quicksand:wght@700&family=Saira+Condensed:wght@800&display=swap">
<style>
  :root {
    --poster-bg: #1c1c1e;
    --brand-blue: #1f8fc6;
    --band-white: #ffffff;
    --line-white: #ffffff;
    --execution: #58585b;
    --innovation: #662d91;
    --loyalty: #262262;
    --synergy: #1f8fc6;
    --growth: #8b5e3c;
    --ethics: #ec008c;
    --love: #ed1c24;
    --placeholder-tone: rgba(255, 255, 255, 0.14);
  }
  html, body {
    margin: 0;
    padding: 0;
    width: 900px;
    height: 1200px;
    overflow: hidden;
    background: var(--poster-bg);
  }
  .poster {
    position: relative;
    width: 900px;
    height: 1200px;
    background: radial-gradient(ellipse at 50% 40%, #242426 0%, var(--poster-bg) 70%);
  }
  .brand {
    position: absolute;
    top: 38px;
    left: 0;
    width: 900px;
    display: flex;
    justify-content: center;
    align-items: center;
    gap: 22px;
  }
  .brand-mark {
    width: 78px;
    height: 78px;
    background: var(--brand-blue);
  }
  .brand-name {
    font-family: "Quicksand", sans-serif;
    font-weight: 700;
    font-size: 82px;
    letter-spacing: 6px;
    color: var(--brand-blue);
    line-height: 1;
  }
  .title {
    position: absolute;
    top: 160px;
    left: 0;
    width: 900px;
    margin: 0;
    text-align: center;
    font-family: "Saira Condensed", sans-serif;
    font-weight: 800;
    font-size: 64px;
    letter-spacing: 2px;
    color: var(--brand-blue);
  }
  .values {
    position: absolute;
    top: 0;
    left: 0;
  }
  .value-label {
    font-family: "Quicksand", sans-serif;
    font-weight: 700;
    font-size: 26px;
    text-anchor: middle;
  }
  .value-label.small { font-size: 22px; }
  .band { fill: var(--band-white); }
  .icon {
    fill: none;
    stroke: var(--line-white);
    stroke-width: 2.5;
    stroke-linejoin: round;
    stroke-linecap: round;
  }
  .gear-teeth {
    fill: none;
    stroke: var(--line-white);
    stroke-width: 9;
  }
  .placeholder { fill: var(--placeholder-tone); }
</style>
</head>
<body>
<main class="poster">
  <header class="brand">
    <div class="brand-mark"></div>
    <div class="brand-name">CLEARVIEW</div>
  </header>
  <h1 class="title">CORE VALUES</h1>

  <svg class="values" width="900" height="1200" viewBox="0 0 900 1200" xmlns="http://www.w3.org/2000/svg">
    <defs>
      <polygon id="hex" points="-157,0 -79,-127 79,-127 157,0 79,127 -79,127"/>
      <polygon id="band" points="-121,59 121,59 100,93 -100,93"/>
    </defs>

    <!-- Execution: gears with bulb -->
    <g class="value value-execution" transform="translate(451 448)">
      <use href="#hex" fill="var(--execution)"/>
      <g class="icon-execution">
        <circle class="gear-teeth" cx="-22" cy="-5" r="42" stroke-dasharray="9 8"/>
        <circle class="icon" cx="-22" cy="-5" r="37" fill="var(--execution)"/>
        <circle class="icon" cx="-22" cy="-5" r="24"/>
        <circle class="icon" cx="-22" cy="-10" r="9"/>
        <path class="icon" d="M-27 -2 L-27 6 L-17 6 L-17 -2 M-25 10 L-19 10"/>
        <circle class="gear-teeth" cx="34" cy="-66" r="26" stroke-dasharray="7 6"/>
        <circle class="icon" cx="34" cy="-66" r="22" fill="var(--execution)"/>
        <circle class="icon" cx="34" cy="-66" r="9"/>
      </g>
      <use href="#band" class="band"/>
      <text class="value-label" y="85" fill="var(--execution)">Execution</text>
    </g>

    <!-- Innovation: bulb half gear -->
    <g class="value value-innovation" transform="translate(203 582)">
      <use href="#hex" fill="var(--innovation)"/>
      <g class="icon-innovation">
        <path class="gear-teeth" d="M0 -92 A46 46 0 0 0 0 0" stroke-dasharray="8 7"/>
        <path class="icon" d="M0 -88 A42 42 0 0 0 0 -4 Z" fill="var(--innovation)"/>
        <path class="icon" d="M0 -64 A18 18 0 0 0 0 -28"/>
        <path class="icon" d="M0 -88 A40 40 0 0 1 38 -48 C38 -24 22 -14 20 6 L0 6"/>
        <path class="icon" d="M-16 14 L16 14 M-16 22 L16 22 M-16 30 L16 30 M-8 38 L8 38"/>
      </g>
      <use href="#band" class="band"/>
      <text class="value-label" y="85" fill="var(--innovation)">Innovation</text>
    </g>

    <!-- Loyalty -->
    <g class="value value-loyalty" transform="translate(699 582)">
      <use href="#hex" fill="var(--loyalty)"/>
      <rect class="placeholder" x="-34" y="-96" width="68" height="140" rx="14" role="img" aria-label="Line pictogram of a standing figure with a heart on the chest and one arm raised"/>
      <use href="#band" class="band"/>
      <text class="value-label" y="85" fill="var(--loyalty)">Loyalty</text>
    </g>

    <!-- Synergy: linked nodes in a ring -->
    <g class="value value-synergy" transform="translate(451 717)">
      <use href="#hex" fill="var(--synergy)"/>
      <g class="icon-synergy">
        <circle class="icon" cx="0" cy="-25" r="62"/>
        <circle class="icon" cx="0" cy="-25" r="42"/>
        <circle class="icon" cx="0" cy="-67" r="9" fill="var(--synergy)"/>
        <circle class="icon" cx="40" cy="-38" r="9" fill="var(--synergy)"/>
        <circle class="icon" cx="25" cy="9" r="9" fill="var(--synergy)"/>
        <circle class="icon" cx="-25" cy="9" r="9" fill="var(--synergy)"/>
        <circle class="icon" cx="-40" cy="-38" r="9" fill="var(--synergy)"/>
      </g>
      <use href="#band" class="band"/>
      <text class="value-label" y="85" fill="var(--synergy)">Synergy</text>
    </g>

    <!-- Growth: bars with rising arrow -->
    <g class="value value-growth" transform="translate(203 849)">
      <use href="#hex" fill="var(--growth)"/>
      <g class="icon-growth">
        <rect class="icon" x="-52" y="20" width="14" height="20"/>
        <rect class="icon" x="-32" y="14" width="14" height="26"/>
        <rect class="icon" x="-12" y="6" width="14" height="34"/>
        <rect class="icon" x="8" y="-6" width="14" height="46"/>
        <rect class="icon" x="28" y="-22" width="14" height="62"/>
        <path class="icon" d="M-56 6 Q10 0 26 -64"/>
        <path class="icon" d="M40 -60 L42 -66 L26 -92 L4 -70 L12 -68 Q0 -18 -56 -4"/>
      </g>
      <use href="#band" class="band"/>
      <text class="value-label small" y="84" fill="var(--growth)">Growth-Oriented</text>
    </g>

    <!-- Ethics: balance scales -->
    <g class="value value-ethics" transform="translate(699 849)">
      <use href="#hex" fill="var(--ethics)"/>
      <g class="icon-ethics">
        <circle class="icon" cx="0" cy="-90" r="5"/>
        <path class="icon" d="M-4 -84 L-4 24 M4 -84 L4 24"/>
        <path class="icon" d="M-56 -72 Q0 -78 56 -72"/>
        <path class="icon" d="M-56 -72 L-72 -30 M-56 -72 L-40 -30 M-74 -30 L-38 -30 Q-56 -12 -74 -30 Z"/>
        <path class="icon" d="M56 -72 L40 -30 M56 -72 L72 -30 M38 -30 L74 -30 Q56 -12 38 -30 Z"/>
        <rect class="icon" x="-26" y="24" width="52" height="12"/>
        <rect class="icon" x="-38" y="36" width="76" height="12"/>
      </g>
      <use href="#band" class="band"/>
      <text class="value-label small" y="84" fill="var(--ethics)">Ethics &amp; Integrity</text>
    </g>

    <!-- Love & Energy: heart with bolt -->
    <g class="value value-love" transform="translate(451 986)">
      <use href="#hex" fill="var(--love)"/>
      <g class="icon-love">
        <path class="icon" stroke-width="3" d="M0 42 C-62 0 -68 -40 -46 -62 C-30 -78 -8 -72 0 -52 C8 -72 30 -78 46 -62 C68 -40 62 0 0 42 Z"/>
        <path class="icon" d="M0 28 C-48 -4 -54 -36 -36 -52 C-24 -62 -8 -58 0 -40 C8 -58 24 -62 36 -52 C54 -36 48 -4 0 28 Z"/>
        <polygon class="icon" fill="var(--line-white)" points="6,-46 -14,-14 2,-14 -8,14 18,-22 2,-22 12,-46"/>
      </g>
      <use href="#band" class="band"/>
      <text class="value-label" y="85" fill="var(--love)">Love &amp; Energy</text>
    </g>
  </svg>
</main>
</body>
</html>
```